Varnek Group Business Card

Varnek Group — Business Card Design Brief
Overview
Design a double-sided business card for Varnek Group that highlights our two service arms: Varnek Communications (telecommunications) and Varnek Energy (business energy solutions). The card should feel smart and stand out when handed to clients.

Objectives
Showcase our areas of specialty clearly.
Reflect the overall Varnek / Varnek Group brand while acknowledging both arms.
Explore using both logos (Communications + Energy) or one unified logo, depending on the design.

Deliverables
One double-sided business card design (front + back).

Content & Copy
Front (preferred): Logo: Varnek / Varnek Group
Descriptor: Business Communications | Business Energy
Back:My contact details and company details
Core products: Business Mobile • Telephony • Internet • Business Energy Solutions

Brand & Visual Direction
We have a group logo currently tailored more toward telecoms, plus a separate Varnek Energy logo.
Please explore layouts that use both logos or just one, whichever works best.
Color: I wouldn't mind seeing an option using our the Blue/Purple gradient from our website (varnek-example.co.uk), but also open to non-gradient approaches and other colours..

Overall look: Smart, modern, and distinctive.
Format & Print Specs
Double-sided business card format. (Use a standard size

Must-Haves
Front: Varnek wording or Varnek Group wording with atleast 1 logo also on front “Business Communications | Business Energy.”

Back: Contact + company details and core products.
A design that stands out while remaining professional.

Nice-to-Have Options
A gradient version using our site’s Blue/Purple gradient.
A non-gradient version.
A dual-logo treatment versus a single-logo treatment.

Thanks
Dominic

```html
<!DOCTYPE html>
<html lang="en">
<head>
<meta charset="utf-8">
<title>Varnek Group Business Card</title>
<link rel="stylesheet" href="https://fonts.googleapis.com/css2?family=Montserrat:wght@400;500;700;800&display=swap">
<style>
  :root {
    --page: #4a4a4c;
    --navy: #24246a;
    --wave-blue: #2f6fbf;
    --sky: #1fa3e0;
    --lime: #c8d62b;
    --green: #4fb848;
    --purple: #8b3f9f;
    --ocean: #146aa6;
    --white: #ffffff;
    --ink: #333333;
  }
  * { box-sizing: border-box; margin: 0; padding: 0; }
  html, body { width: 1200px; height: 875px; overflow: hidden; }
  body {
    background: var(--page);
    font-family: "Montserrat", sans-serif;
    position: relative;
  }
  .card {
    position: absolute;
    left: 260px;
    width: 680px;
    height: 389px;
    overflow: hidden;
    box-shadow: 0 10px 30px rgba(0,0,0,0.35);
  }

  /* Front */
  .card-front {
    top: 28px;
    background: linear-gradient(120deg, var(--purple) 0%, #5f5aa6 45%, var(--ocean) 100%);
  }
  .front-brands {
    position: absolute;
    top: 120px; left: 0; right: 0;
    display: flex;
    justify-content: center;
    align-items: center;
    gap: 48px;
  }
  .brand {
    display: flex;
    align-items: center;
    gap: 14px;
    font-weight: 700;
    font-size: 40px;
    letter-spacing: 1px;
  }
  .brand-dot {
    width: 44px; height: 44px;
    border-radius: 50%;
    flex: none;
  }
  .brand-comms { color: var(--sky); }
  .brand-comms .brand-dot { background: var(--sky); }
  .brand-energy { color: var(--lime); }
  .brand-energy .brand-dot { background: var(--green); }
  .front-divider {
    width: 1px; height: 90px;
    background: var(--lime);
  }
  .descriptor {
    position: absolute;
    top: 262px; left: 0; right: 0;
    text-align: center;
    font-size: 19px;
    font-weight: 500;
    letter-spacing: 0.5px;
  }
  .descriptor .comms { color: var(--sky); }
  .descriptor .energy { color: var(--lime); }

  /* Back */
  .card-back {
    top: 458px;
    background: var(--white);
  }
  .back-wave { position: absolute; inset: 0; }
  .back-brands {
    position: absolute;
    top: 128px; left: 40px;
    display: flex;
    gap: 34px;
  }
  .back-brand {
    display: flex;
    align-items: center;
    gap: 8px;
    font-weight: 800;
    font-size: 28px;
    color: var(--navy);
  }
  .back-brand .brand-dot { width: 24px; height: 24px; }
  .back-brand.comms .brand-dot { background: var(--sky); }
  .back-brand.energy .brand-dot { background: var(--green); }
  .person {
    position: absolute;
    top: 24px; right: 34px;
    text-align: right;
    color: var(--navy);
  }
  .person-name { font-weight: 800; font-size: 25px; letter-spacing: 0.5px; }
  .person-role { font-weight: 500; font-size: 14px; color: var(--ink); margin-top: 2px; }
  .contact {
    position: absolute;
    right: 28px; top: 168px;
    list-style: none;
    text-align: right;
    color: var(--white);
    font-size: 14px;
    line-height: 1.6;
  }
  .contact li { display: flex; justify-content: flex-end; align-items: center; gap: 8px; }
  .contact svg { width: 11px; height: 11px; fill: var(--sky); flex: none; }
  .products {
    position: absolute;
    left: 40px; bottom: 28px;
    color: var(--white);
    font-size: 14px;
    line-height: 1.7;
  }
  .products span::before {
    content: "•";
    color: var(--sky);
    margin: 0 4px 0 8px;
  }
  .products .row span:first-child::before { margin-left: 0; }
</style>
</head>
<body>

<section class="card card-front" aria-label="Business card front">
  <div class="front-brands">
    <div class="brand brand-comms"><span class="brand-dot"></span>Varnek</div>
    <div class="front-divider"></div>
    <div class="brand brand-energy"><span class="brand-dot"></span>Varnek</div>
  </div>
  <p class="descriptor"><span class="comms">Business Communications</span> <span class="energy">| Business Energy</span></p>
</section>

<section class="card card-back" aria-label="Business card back">
  <svg class="back-wave" viewBox="0 0 680 389" preserveAspectRatio="none" aria-hidden="true">
    <path d="M30,212 C200,258 325,228 395,156 C452,98 525,90 610,94 L610,99 C528,98 462,110 408,164 C332,242 200,272 30,226 Z" fill="var(--wave-blue)"/>
    <path d="M0,236 C180,290 330,262 410,180 C470,120 560,110 680,108 L680,389 L0,389 Z" fill="var(--navy)"/>
    <path d="M170,300 C300,298 375,258 425,204 C475,148 545,128 640,124" stroke="var(--white)" stroke-width="1.5" fill="none"/>
  </svg>

  <div class="back-brands">
    <div class="back-brand comms"><span class="brand-dot"></span>Varnek</div>
    <div class="back-brand energy"><span class="brand-dot"></span>Varnek</div>
  </div>

  <div class="person">
    <div class="person-name">COLIN MARSH</div>
    <div class="person-role">Founder/CEO</div>
  </div>

  <ul class="contact">
    <li>24 Alder Row</li>
    <li>Leeds England, LS2 7QP</li>
    <li>+44 0113 555 0142 <svg viewBox="0 0 24 24"><path d="M6.6 10.8a15 15 0 0 0 6.6 6.6l2.2-2.2a1 1 0 0 1 1-.25 11.4 11.4 0 0 0 3.6.57 1 1 0 0 1 1 1V20a1 1 0 0 1-1 1A17 17 0 0 1 3 4a1 1 0 0 1 1-1h3.5a1 1 0 0 1 1 1c0 1.25.2 2.45.57 3.57a1 1 0 0 1-.25 1z"/></svg></li>
    <li>info@varnek-example.co.uk <svg viewBox="0 0 24 24"><rect x="2" y="5" width="20" height="14" rx="2"/></svg></li>
    <li>www.varnek-example.co.uk <svg viewBox="0 0 24 24"><circle cx="12" cy="12" r="10"/></svg></li>
  </ul>

  <div class="products">
    <div class="row"><span>Business Mobile</span><span>Internet</span></div>
    <div class="row"><span>Telephony</span><span>Business Energy Solutions</span></div>
  </div>
</section>

</body>
</html>
```